Flyer-Design für Designer-Schmuck
Zielgruppe
Wir produzieren außergewöhnlichen und hochwertigen Designer-Schmuck aus Lüster-Bleikristallen für eine modebewusstes Publikum. Der Flyer wird als Beipack-Flyer unseren Versendungen beigefügt und enthält Informationen, sowie Hinweise für unsere Kunden über Glanzwerk, zu Nachhaltigkeit und Pflege.
Aufgabenstellung
nicht größer als DIN A5 | mindestens 2 oder mehr Seiten | Sollte die Aufteilung der Texte 6 Seiten erfordern sind auch 6 Seiten in Ordnung | Design und Layout sind sonst wenig Grenzen gesetzt - wir lassen uns gerne von Euren Vorschlägen begeistern, gerne aber mit Wiedererkennungswert zur Webseite https://glanzwerk-atelier.example

```html
<!DOCTYPE html>
<html lang="de">
<head>
<meta charset="utf-8">
<title>Glanzwerk Hamburg – Beipack-Flyer</title>
<link href="https://fonts.googleapis.com/css2?family=Montserrat:wght@400;500;600;700&display=swap" rel="stylesheet">
<style>
  :root {
    --purple: #7d2b8c;
    --purple-soft: #9a56a6;
    --paper: #f4f3f5;
    --paper-edge: #e4e2e6;
    --ink: #5a5560;
    --ground: #ece8e6;
    --photo-dark: #6f6a66;
    --photo-light: #d9d4cf;
  }
  * { box-sizing: border-box; margin: 0; padding: 0; }
  html, body { width: 1035px; height: 1200px; overflow: hidden; }
  body {
    background: var(--ground);
    font-family: "Montserrat", sans-serif;
    color: var(--ink);
    position: relative;
  }
  .trifold {
    position: absolute; top: 40px; left: 22px;
    width: 990px; height: 500px;
    display: flex;
    box-shadow: 0 2px 10px rgba(0,0,0,.08);
  }
  .panel {
    width: 330px; height: 500px;
    background: var(--paper);
    border-right: 1px solid var(--paper-edge);
    padding: 36px 30px;
    display: flex; flex-direction: column;
  }
  .panel:last-child { border-right: none; }

  /* cover */
  .cover { align-items: center; justify-content: center; text-align: center; }
  .brand { display: flex; flex-direction: column; align-items: center; }
  .brand-dot {
    width: 96px; height: 96px; border-radius: 50%;
    background: var(--purple); margin-bottom: 22px;
  }
  .brand-name {
    font-size: 40px; font-weight: 600; color: var(--purple);
    line-height: 1; letter-spacing: .5px;
  }
  .brand-city {
    font-size: 15px; font-weight: 400; color: var(--purple);
    letter-spacing: 6px; margin-top: 8px;
  }
  .cover-sub {
    margin-top: 54px; font-size: 9px; font-weight: 600;
    letter-spacing: 1.5px; text-transform: uppercase; color: var(--purple-soft);
  }
  .tagline {
    margin-top: 6px; font-size: 15px; font-weight: 600;
    letter-spacing: 2px; color: var(--purple);
  }

  /* intro */
  .section-title {
    font-size: 15px; font-weight: 600; letter-spacing: 2px;
    color: var(--purple); text-transform: uppercase; line-height: 1.35;
  }
  .collage {
    margin-top: 20px;
    display: grid; grid-template-columns: 1fr 1fr; grid-template-rows: 120px 120px;
    gap: 6px;
  }
  .collage .photo:nth-child(1) { background: linear-gradient(135deg, var(--photo-light), #b8b1aa); }
  .collage .photo:nth-child(2) { background: linear-gradient(135deg, #c9c3bc, var(--photo-dark)); }
  .collage .photo:nth-child(3) { background: linear-gradient(135deg, #8b847e, #c8b79a); }
  .collage .photo:nth-child(4) { background: linear-gradient(135deg, var(--photo-dark), #a69d94); }
  .notes { margin-top: 26px; list-style: none; }
  .notes li {
    font-size: 10px; color: var(--purple); margin-bottom: 10px;
    display: flex; align-items: center; gap: 8px;
  }
  .notes li::before {
    content: ""; width: 6px; height: 6px; border-radius: 50%; background: var(--purple);
  }

  /* story */
  .body-text {
    margin-top: 18px; font-size: 10.5px; line-height: 1.7; color: var(--ink);
  }
  .features { margin-top: auto; display: flex; justify-content: space-between; }
  .feature { display: flex; flex-direction: column; align-items: center; gap: 8px; width: 80px; }
  .feature-icon {
    width: 52px; height: 52px; border-radius: 50%; background: var(--purple);
    display: flex; align-items: center; justify-content: center;
  }
  .feature-label { font-size: 9px; font-weight: 600; color: var(--purple); text-transform: uppercase; letter-spacing: 1px; }

  /* single card */
  .card {
    position: absolute; top: 600px; left: 352px;
    width: 330px; height: 460px;
    background: var(--paper);
    box-shadow: 0 2px 10px rgba(0,0,0,.08);
    display: flex; flex-direction: column; align-items: center; justify-content: center;
    text-align: center;
  }
</style>
</head>
<body>

<section class="trifold">
  <div class="panel cover">
    <div class="brand">
      <span class="brand-dot"></span>
      <span class="brand-name">Glanzwerk</span>
      <span class="brand-city">HAMBURG</span>
    </div>
    <p class="cover-sub">Handgemachter Lüsterschmuck aus Hamburg</p>
    <p class="tagline">SO EINZIGARTIG WIE DU</p>
  </div>

  <div class="panel intro">
    <h2 class="section-title">Lerne uns kennen</h2>
    <div class="collage">
      <div class="photo" role="img" aria-label="Foto: Kristallschmuck in Nahaufnahme"></div>
      <div class="photo" role="img" aria-label="Foto: funkelnder Kronleuchter"></div>
      <div class="photo" role="img" aria-label="Foto: Werkstatt mit Lüsterkristallen"></div>
      <div class="photo" role="img" aria-label="Foto: Schmuckstück am Ohr getragen"></div>
    </div>
    <ul class="notes">
      <li>Kristalle aus Hamburg</li>
      <li>Jedes Stück ein Unikat</li>
      <li>Sorgsam verpackt</li>
    </ul>
  </div>

  <div class="panel story">
    <h2 class="section-title">Einzigartige Lüsterkristalle<br>Schmuckstücke für dich</h2>
    <p class="body-text">Jedes Schmuckstück entsteht in Handarbeit aus echten Lüster-Bleikristallen, die einst große Säle zum Funkeln brachten. Wir geben ihnen ein zweites Leben und verbinden historischen Glanz mit modernem Design. So trägst du ein Unikat, das Geschichte erzählt und Ressourcen schont. Pflege deine Kristalle mit einem weichen Tuch und bewahre sie trocken auf.</p>
    <div class="features">
      <div class="feature">
        <span class="feature-icon">
          <svg width="24" height="24" viewBox="0 0 24 24" fill="none" stroke="#fff" stroke-width="2.2" stroke-linecap="round" stroke-linejoin="round"><path d="M5 12.5l4.5 4.5L19 7.5"/></svg>
        </span>
        <span class="feature-label">Handarbeit</span>
      </div>
      <div class="feature">
        <span class="feature-icon">
          <svg width="24" height="24" viewBox="0 0 24 24" fill="none" stroke="#fff" stroke-width="2" stroke-linecap="round" stroke-linejoin="round"><path d="M5 19C5 10 11 5 19 5c0 8-5 14-14 14z"/><path d="M5 19l8-8"/></svg>
        </span>
        <span class="feature-label">Nachhaltig</span>
      </div>
      <div class="feature">
        <span class="feature-icon">
          <svg width="24" height="24" viewBox="0 0 24 24" fill="none" stroke="#fff" stroke-width="2" stroke-linejoin="round"><path d="M12 3C9 8 6 11 6 14.5a6 6 0 0 0 12 0C18 11 15 8 12 3z"/></svg>
        </span>
        <span class="feature-label">Pflege</span>
      </div>
    </div>
  </div>
</section>

<section class="card">
  <div class="brand">
    <span class="brand-dot"></span>
    <span class="brand-name">Glanzwerk</span>
    <span class="brand-city">HAMBURG</span>
  </div>
  <p class="cover-sub">Handgemachter Lüsterschmuck aus Hamburg</p>
  <p class="tagline">SO EINZIGARTIG WIE DU</p>
</section>

</body>
</html>
```